Name card for fertilizer industry

We 1. produce liquid fertilizer 2. gardening supply 3. Import&Export gardening related product.
I want the name card double-sided(Chinese & English version)
detail has chinese charactor for name and address.
Updates
Target Market(s)
Farmers
Industry/Entity Type
Industry
Contact Information for Business Card
Name: Daniel Lo (陳明達)
TEL: +886-48-516042
FAX:+886-48-590714
MOBILE: +886-912-804-153
ADDRESS: No.58, Baoan Rd, Dapu Township, Kexi County , TAIWAN(R.O.C) 柯溪縣大埔鎮寶安路58號
Look and feel
Each slider illustrates characteristics of the customer's brand and the style your logo design should communicate.

```html
<!DOCTYPE html>
<html lang="en">
<head>
<meta charset="UTF-8">
<title>Maplevale Enterprise Co. – Name Cards</title>
<link rel="stylesheet" href="https://fonts.googleapis.com/css2?family=Ubuntu:wght@400;500&family=Noto+Sans+TC:wght@400;500&display=swap">
<style>
  :root {
    --backdrop: #3b3b3b;
    --card-brown: #716558;
    --card-white: #ffffff;
    --leaf-green: #72a03a;
    --leaf-light: #9cc83f;
    --ink-brown: #6b6157;
    --text-light: #ffffff;
  }
  * { margin: 0; padding: 0; box-sizing: border-box; }
  html, body { width: 1200px; height: 1000px; overflow: hidden; }
  body {
    background: var(--backdrop);
    font-family: "Ubuntu", "Noto Sans TC", sans-serif;
    position: relative;
  }
  .card { position: absolute; width: 520px; height: 304px; overflow: hidden; }
  .card--back {
    left: 339px; top: 135px; width: 522px; height: 305px;
    background: var(--card-brown);
  }
  .card--english { left: 58px; top: 549px; }
  .card--chinese { left: 622px; top: 549px; }

  .brand-mark {
    position: absolute; border-radius: 50%;
    background: linear-gradient(135deg, var(--leaf-light), var(--leaf-green));
  }
  .card--back .brand-mark { width: 150px; height: 150px; left: 186px; top: 78px; }
  .card--back .back-name {
    position: absolute; left: 0; right: 0; top: 240px; text-align: center;
    color: var(--text-light); font-size: 15px; letter-spacing: 0.5px;
  }

  .face-top {
    position: absolute; left: 0; top: 0; width: 100%; height: 171px;
    background: var(--card-white);
  }
  .face-top .brand-mark { width: 78px; height: 78px; left: 221px; top: 26px; }
  .company-name {
    position: absolute; left: 0; right: 0; top: 106px; text-align: center;
    color: var(--ink-brown); font-size: 16px; letter-spacing: 0.2px;
  }
  .tagline {
    position: absolute; left: 40px; right: 40px; top: 131px; text-align: center;
    color: var(--leaf-green); font-size: 12px; line-height: 14px;
  }
  .name-band {
    position: absolute; left: 0; top: 171px; width: 100%; height: 30px;
    background: var(--leaf-green); color: var(--text-light);
    text-align: center; font-size: 20px; line-height: 30px; font-weight: 500;
    letter-spacing: 1.5px;
  }
  .card--chinese .name-band { font-family: "Noto Sans TC", sans-serif; font-weight: 400; letter-spacing: 2px; }
  .face-bottom {
    position: absolute; left: 0; top: 201px; width: 100%; height: 103px;
    background: var(--card-brown); color: var(--text-light);
  }
  .contact-list { position: absolute; left: 35px; top: 20px; list-style: none; font-size: 12.5px; }
  .contact-list li { display: flex; align-items: center; height: 18px; }
  .contact-list svg { width: 15px; height: 15px; margin-right: 8px; }
  .address { position: absolute; left: 294px; top: 22px; font-size: 12px; line-height: 18px; }
  .card--chinese .address { left: 295px; top: 17px; font-family: "Noto Sans TC", sans-serif; }
</style>
</head>
<body>
  <section class="card card--back">
    <div class="brand-mark"></div>
    <p class="back-name">MAPLEVALE ENTERPRISE CO.</p>
  </section>

  <section class="card card--english">
    <div class="face-top">
      <div class="brand-mark"></div>
      <h1 class="company-name">MAPLEVALE ENTERPRISE CO.</h1>
      <p class="tagline">Production of Liquid Fertilizer - Gardening Supply - Import &amp; Export of Gardening Related Products</p>
    </div>
    <div class="name-band">DANIEL LO</div>
    <div class="face-bottom">
      <ul class="contact-list">
        <li><svg viewBox="0 0 16 16"><circle cx="8" cy="8" r="8" fill="#72a03a"/><path d="M5 4.5l1.5-.5 1 2-1 .8a5 5 0 0 0 2.7 2.7l.8-1 2 1-.5 1.5C9 11.5 4.5 7 5 4.5z" fill="#fff"/></svg>+886-48-516042</li>
        <li><svg viewBox="0 0 16 16"><circle cx="8" cy="8" r="8" fill="#72a03a"/><rect x="5.5" y="4" width="5" height="2.5" fill="#fff"/><rect x="4" y="6.5" width="8" height="4" rx="1" fill="#fff"/><rect x="5.5" y="9.5" width="5" height="2.5" fill="#fff" stroke="#72a03a" stroke-width=".6"/></svg>+886-48-590714</li>
        <li><svg viewBox="0 0 16 16"><circle cx="8" cy="8" r="8" fill="#72a03a"/><rect x="5.5" y="3.5" width="5" height="9" rx="1" fill="#fff"/><rect x="6.3" y="4.6" width="3.4" height="6" fill="#72a03a"/></svg>+886-912-804-153</li>
      </ul>
      <p class="address">No.58, Baoan Rd,<br>Dapu Township,<br>Kexi County, TAIWAN (R.O.C)</p>
    </div>
  </section>

  <section class="card card--chinese">
    <div class="face-top">
      <div class="brand-mark"></div>
      <h1 class="company-name">MAPLEVALE ENTERPRISE CO.</h1>
      <p class="tagline">Production of Liquid Fertilizer - Gardening Supply - Import &amp; Export of Gardening Related Products</p>
    </div>
    <div class="name-band">陳明達</div>
    <div class="face-bottom">
      <ul class="contact-list">
        <li><svg viewBox="0 0 16 16"><circle cx="8" cy="8" r="8" fill="#72a03a"/><path d="M5 4.5l1.5-.5 1 2-1 .8a5 5 0 0 0 2.7 2.7l.8-1 2 1-.5 1.5C9 11.5 4.5 7 5 4.5z" fill="#fff"/></svg>+886-48-516042</li>
        <li><svg viewBox="0 0 16 16"><circle cx="8" cy="8" r="8" fill="#72a03a"/><rect x="5.5" y="4" width="5" height="2.5" fill="#fff"/><rect x="4" y="6.5" width="8" height="4" rx="1" fill="#fff"/><rect x="5.5" y="9.5" width="5" height="2.5" fill="#fff" stroke="#72a03a" stroke-width=".6"/></svg>+886-48-590714</li>
        <li><svg viewBox="0 0 16 16"><circle cx="8" cy="8" r="8" fill="#72a03a"/><rect x="5.5" y="3.5" width="5" height="9" rx="1" fill="#fff"/><rect x="6.3" y="4.6" width="3.4" height="6" fill="#72a03a"/></svg>+886-912-804-153</li>
      </ul>
      <p class="address">柯溪縣大埔鎮寶安路58號</p>
    </div>
  </section>
</body>
</html>
```